Design 5 colour schemes for one web page

We are looking for 5 different colour schemes for our product template to create different kinds of colour tone for our web page, it doesn't need to be restructure the layout, just need to provide different color solution.

Please refer to the attached images and take note of the following when you’re working on the design:
(1) Please precisely reproduce the layout. Cannot remove or delete any wordings, components or column shown in the images.
(2) Okay to revise icons, background color or text style as you prefer. But cannot move/delete them.
(3) Provide PSD source files with good layer management. HTML/CSS are not required.
(4) Make reasonable and professional design.

After completion, please send back:
(1) 5 images with 5 different colour schemes.
(2) Related PSD files.

Font styles to use
Serif
Sans Serif

Requirements
Must have
• (1) 5 images for the colour schemes.
• (2) 5 PSD source files with good layer management.
Nice to have
• (1) Explanation about your design of the colour schemes.
Should not have
• (1) HTML/CSS code are not required.

```html
<!DOCTYPE html>
<html lang="en">
<head>
<meta charset="utf-8">
<title>Sportsbook – Live Odds (Midnight Teal scheme)</title>
<link rel="stylesheet" href="https://fonts.googleapis.com/css2?family=Roboto:ital,wght@0,400;0,500;1,400&display=swap">
<style>
:root{
  --bg-deep:#0b111b;
  --bar-top:#121a28;
  --panel:#1b2536;
  --toolbar:#111827;
  --side:#1a2334;
  --side-dark:#101724;
  --accent:#16717d;
  --tab:#f2c14e;
  --tab-text:#1b1e24;
  --live:#c4372f;
  --live-row:#4d2630;
  --head:#161f2e;
  --row-a:#222d40;
  --row-b:#1b2537;
  --line:#0a0f18;
  --text:#ffffff;
  --muted:#b9c3d0;
  --home:#8fd6e2;
  --teal:#4fd1c5;
  --orange:#ffb04a;
  --badge:#e8402e;
  --signout:#16717d;
}
*{box-sizing:border-box;margin:0;padding:0}
html,body{width:1155px;height:1200px;overflow:hidden;background:var(--bg-deep)}
body{font-family:"Roboto",Arial,sans-serif;color:var(--text);font-size:14px}
.stage{position:relative;width:1344px;height:1396px;transform:scale(0.859375);transform-origin:0 0}
.backdrop{position:absolute;inset:0;background:radial-gradient(ellipse at 50% 30%,#1f2a3b 0%,#111927 55%,#080c13 100%)}
.abs{position:absolute}
.ico{fill:none;stroke:var(--text);stroke-width:1.6;stroke-linecap:round;stroke-linejoin:round}
.ico .f{fill:var(--text);stroke:none}

/* top bar */
.topbar{left:0;top:0;width:1344px;height:40px;background:var(--bar-top)}
.topbar a{position:absolute;top:11px;color:var(--text);text-decoration:none;font-size:14px}
.badge{background:var(--badge);border-radius:9px;padding:0 5px;font-size:12px;margin-left:4px}
.balance{left:992px;top:7px;width:158px;height:27px;background:#222c3c;border-radius:3px;font-size:14px;padding:5px 10px}
.signout{left:1162px;top:7px;width:81px;height:27px;background:var(--signout);border-radius:3px;text-align:center;padding-top:5px}

/* header */
.header{left:100px;top:40px;width:1144px;height:100px;background:var(--panel)}
.logo{left:125px;top:58px;font-size:46px;font-weight:500;letter-spacing:1px}
.sports-tab{left:393px;top:79px;width:114px;height:61px;background:var(--tab);color:var(--tab-text);font-weight:500;font-size:16px;text-align:center;padding-top:21px}
.results{left:1155px;top:56px;font-size:12px}
.toolbar{left:100px;top:140px;width:1144px;height:40px;background:var(--toolbar);font-size:12px}
.toolbar .t{position:absolute;top:13px}
.toolbar .sep{position:absolute;top:0;width:1px;height:40px;background:#263043}
.toolbar svg{position:absolute}

/* sidebar */
.sb-head{left:100px;width:210px;height:30px;background:var(--accent);text-align:center;padding-top:6px;font-size:14px}
.fav-box{left:100px;top:220px;width:210px;height:92px;background:var(--side)}
.fav-box div{position:absolute;left:14px;top:12px;width:180px;height:68px;border:1px dashed #7e8897;font-size:12px;text-align:center;padding-top:16px;line-height:18px}
.fav-box em{font-style:normal;color:var(--tab)}
.tabs{left:100px;width:210px;height:30px;background:var(--side)}
.tabs .on{position:absolute;left:28px;top:6px}
.tabs .off{position:absolute;right:0;top:0;width:118px;height:30px;background:var(--tab);color:var(--tab-text);clip-path:polygon(0 0,100% 0,100% 100%,28px 100%);padding:8px 0 0 50px}
.sport-list{left:100px;top:360px;width:210px}
.sport{height:30px;background:var(--side);border-bottom:1px solid var(--line);position:relative;padding:6px 0 0 32px;font-size:14px}
.sport svg{position:absolute;left:10px;top:7px}
.sport .n{position:absolute;right:10px;top:3px;width:42px;height:23px;background:var(--side-dark);color:var(--muted);text-align:center;padding-top:3px}
.bar-under{left:100px;top:1010px;width:210px;height:4px;background:#3f4a5c}
.mybets{left:100px;top:1055px;width:210px;height:85px;background:var(--side)}
.refresh-s{left:172px;top:1069px;font-size:12px}
.pending{left:128px;top:1100px;width:161px;height:26px;background:#2c374a;border-radius:2px;font-size:12px;font-style:italic;color:var(--muted);text-align:center;padding-top:5px}
.viewall{left:100px;top:1150px;width:210px;height:30px;background:var(--side);text-align:center;padding-top:7px}

/* main tables */
.board{left:323px;width:921px}
.board-bar{height:30px;background:var(--bar-top);position:relative}
.board-bar .tab{position:absolute;left:0;top:0;height:30px;width:150px;padding:7px 0 0 31px;clip-path:polygon(0 0,120px 0,150px 100%,0 100%)}
.board-bar .cnt{position:absolute;left:430px;top:6px}
.board-bar .sel{position:absolute;right:17px;top:7px}
.live-board .board-bar{border-bottom:3px solid var(--live)}
.live-board .tab{background:var(--live)}
.std-board .tab{background:var(--accent)}
.grid{display:grid;grid-template-columns:76px 226px 51px 86px 88px 47px 113px 110px 48px 76px}
.col-head{background:var(--head);height:60px;grid-template-rows:30px 30px}
.col-head > div{display:flex;align-items:center;justify-content:center;border-left:1px solid var(--line);border-bottom:1px solid var(--line)}
.col-head .span2{grid-row:1 / 3}
.col-head .ft{grid-column:3 / 7}
.col-head .fh{grid-column:7 / 10}
.col-head .more{grid-column:10;grid-row:1 / 3}
.league{height:26px;padding:4px 0 0 85px;position:relative;font-size:14px}
.league::after{content:"";position:absolute;right:15px;top:6px;width:13px;height:13px;border:1.5px solid #fff;border-radius:50%;border-top-color:transparent}
.live-board .league{background:var(--live);height:28px;padding-top:5px}
.std-board .league{background:var(--accent)}
.league .star{margin-right:6px}
.event{height:58px;position:relative;border-bottom:1px solid var(--line);background:var(--row-a)}
.event:nth-of-type(even){background:var(--row-b)}
.live-board .event{background:var(--live-row);height:51px}
.event > div{position:absolute;top:0;height:100%;border-right:1px solid var(--line)}
.c-time{left:0;width:75px}
.c-time svg{position:absolute;left:10px;top:20px}
.kick{position:absolute;left:32px;top:10px}
.live{position:absolute;left:37px;top:25px;color:var(--orange);font-style:italic}
.c-event{left:75px;width:227px}
.c-event .star{position:absolute;left:10px;top:18px}
.teams{position:absolute;left:33px;top:1px;line-height:15px;font-size:14px}
.teams span{display:block}
.home{color:var(--home)}
.away{color:var(--orange)}
.live-board .teams{top:10px}
.c-ft{left:302px;width:272px}
.c-ft span{position:absolute}
.hc{left:30px;top:20px;color:var(--teal)}
.odds{line-height:18px}
.odds b{display:block;font-weight:400;color:#fff}
.odds i{display:block;font-style:normal;color:var(--orange)}
.hdp{left:80px;top:12px;text-align:right}
.line{left:132px;top:12px;color:var(--teal)}
.oul{left:181px;top:12px;line-height:18px}
.ou{left:202px;top:12px;text-align:right}
.live-board .c-ft span{top:7px}
.live-board .hc{top:16px!important}
.c-fh{left:574px;width:271px;border-right:none!important}
.c-more{left:845px;width:76px;border-right:none!important;padding:21px 0 0 12px}
.live-board .c-more{padding-top:17px}
.c-more svg{vertical-align:-1px;margin-right:6px}

.footer{left:0;top:1347px;width:1344px;text-align:center;font-size:12px}
.footer span{padding:0 7px;border-left:1px solid #fff}
.footer span:first-child{border-left:none}
</style>
</head>
<body>
<div class="stage">
  <div class="backdrop" role="img" aria-label="Dark stadium crowd photograph behind the page"></div>

  <nav class="topbar abs">
    <a style="left:104px">My Bets</a>
    <a style="left:187px">Statement</a>
    <a style="left:284px">Preference</a>
    <a style="left:383px">Announcements<span class="badge">99+</span></a>
    <a style="left:904px">Hi, usr2041</a>
  </nav>
  <div class="balance abs">» SD$ 10,072.00 ↻</div>
  <div class="signout abs">Sign Out</div>

  <header class="header abs"></header>
  <div class="logo abs">LOGO</div>
  <div class="sports-tab abs">SPORTS</div>
  <div class="results abs">▣ Results</div>
  <div class="toolbar abs">
    <svg class="ico" style="left:16px;top:12px" width="16" height="16"><circle cx="8" cy="8" r="7"/><path d="M1 8h14M8 1c3 3 3 11 0 14M8 1c-3 3-3 11 0 14"/></svg>
    <span class="t" style="left:42px">English (Asia) ▾</span>
    <span class="sep" style="left:155px"></span>
    <span class="t" style="left:175px">12/02/2013 15:53PM GMT +8</span>
    <svg class="ico" style="left:708px;top:13px" width="22" height="14"><rect x="1" y="1" width="20" height="12"/><path d="M11 4v6M8 7h6"/></svg>
    <span class="t" style="left:740px">▾</span>
    <span class="sep" style="left:765px"></span>
    <svg style="left:781px;top:11px" width="18" height="18"><path class="f" d="M9 1l2.4 5.3 5.6.6-4.2 3.8 1.2 5.6L9 13.5 4 16.3l1.2-5.6L1 6.9l5.6-.6z" fill="#fff"/></svg>
    <span class="t" style="left:810px">▾</span>
    <span class="sep" style="left:837px"></span>
    <svg class="ico" style="left:852px;top:13px" width="22" height="14"><rect x="1" y="1" width="20" height="12"/><path d="M5 5h2M9 5h8M5 9h2M9 9h8"/></svg>
    <span class="t" style="left:884px">▾</span>
    <span class="sep" style="left:910px"></span>
    <span class="t" style="left:926px">MY &nbsp;▾</span>
    <span class="sep" style="left:980px"></span>
    <svg class="ico" style="left:997px;top:12px" width="22" height="16"><path class="f" d="M1 5h4l5-4v14l-5-4H1z"/><path d="M13 5c1.5 1.5 1.5 4.5 0 6M16 3c3 3 3 7 0 10"/></svg>
    <span class="sep" style="left:1035px"></span>
    <svg class="ico" style="left:1050px;top:9px" width="22" height="22"><rect x="1" y="7" width="20" height="13" rx="1"/><path d="M7 2l4 5 4-5"/></svg>
    <span class="sep" style="left:1088px"></span>
    <span class="t" style="left:1103px">Live</span>
  </div>

  <aside>
    <div class="sb-head abs" style="top:190px">My Favourites</div>
    <div class="fav-box abs"><div>Click on an event or league<br>to add it to <em>"My Favourites"</em></div></div>
    <div class="tabs abs" style="top:321px"><span class="on">Sport</span><span class="off">Markets</span></div>
    <div class="sport-list abs">
      <div class="sport"><svg class="ico" width="16" height="16"><circle cx="8" cy="8" r="6.5"/><path class="f" d="M8 5l2.5 1.8-1 3H6.5l-1-3z"/></svg>Football<span class="n">600</span></div>
      <div class="sport"><svg class="ico" width="16" height="16"><circle cx="8" cy="8" r="6.5"/><path d="M1.5 8h13M8 1.5v13M3.5 3.5c2.5 2.5 2.5 6.5 0 9M12.5 3.5c-2.5 2.5-2.5 6.5 0 9"/></svg>Basketball<span class="n">600</span></div>
      <div class="sport"><svg class="ico" width="16" height="16"><circle cx="8" cy="8" r="6.5"/><path d="M4 2.8c2 3 2 7.4 0 10.4M12 2.8c-2 3-2 7.4 0 10.4"/></svg>Baseball<span class="n">600</span></div>
      <div class="sport"><svg class="ico" width="16" height="16"><ellipse cx="6.5" cy="6.5" rx="4.5" ry="5" transform="rotate(-45 6.5 6.5)"/><path d="M9.8 9.8l5 5"/></svg>Tennis<span class="n">600</span></div>
      <div class="sport"><svg class="ico" width="16" height="16"><ellipse cx="8" cy="8" rx="7" ry="4" transform="rotate(-35 8 8)"/><path d="M6 10l4-4M7 7l2 2"/></svg>American Football<span class="n">600</span></div>
      <div class="sport"><svg class="ico" width="16" height="16"><circle class="f" cx="11.5" cy="11.5" r="3"/><path d="M10 10L2 6l4-4z"/></svg>Badminton<span class="n">600</span></div>
      <div class="sport"><svg class="ico" width="16" height="16"><path d="M4 14V7a4 4 0 0 1 8 0v2H8v5zM4 14h8"/></svg>Boxing<span class="n">600</span></div>
      <div class="sport"><svg class="ico" width="16" height="16"><path d="M2 14l8-8M8 4l4 4"/><circle class="f" cx="13" cy="13" r="2"/></svg>Cricket<span class="n">600</span></div>
      <div class="sport"><svg class="ico" width="16" height="16"><circle cx="4" cy="11" r="3"/><circle cx="12" cy="11" r="3"/><path d="M4 11l3-5h4l1 5M6 4h3"/></svg>Cycling<span class="n">600</span></div>
      <div class="sport"><svg class="ico" width="16" height="16"><circle cx="8" cy="8" r="6.5"/><circle cx="8" cy="8" r="3.5"/><circle class="f" cx="8" cy="8" r="1.2"/></svg>Dart<span class="n">600</span></div>
      <div class="sport"><svg class="ico" width="16" height="16"><path d="M6 13V3l8-2v10"/><circle class="f" cx="4" cy="13" r="2"/><circle class="f" cx="12" cy="11" r="2"/></svg>Entertainment<span class="n">600</span></div>
      <div class="sport"><svg class="ico" width="16" height="16"><path d="M5 15V1"/><path class="f" d="M5 1l8 3-8 3z"/><path d="M2 15h8"/></svg>Golf<span class="n">600</span></div>
      <div class="sport"><svg class="ico" width="16" height="16"><circle cx="8" cy="8" r="6.5"/><path d="M3 5c3 1 7 1 10 0M3 11c3-1 7-1 10 0"/></svg>Handball<span class="n">600</span></div>
      <div class="sport"><svg class="ico" width="16" height="16"><path d="M11 1L5 13H1"/><rect class="f" x="9" y="12" width="6" height="3" rx="1"/></svg>Ice Hockey<span class="n">600</span></div>
      <div class="sport"><svg class="ico" width="16" height="16"><path d="M5 1h6l4 4v6l-4 4H5l-4-4V5z"/></svg>Mixed Martial Art<span class="n">600</span></div>
      <div class="sport"><svg class="ico" width="16" height="16"><path d="M2 15V1h12v9H2"/><path class="f" d="M2 1h3v3H2zM8 1h3v3H8zM5 4h3v3H5zM11 4h3v3h-3zM2 7h3v3H2zM8 7h3v3H8z"/></svg>Motor Sport<span class="n">600</span></div>
      <div class="sport"><svg class="ico" width="16" height="16"><circle class="f" cx="8" cy="8" r="7"/><circle cx="8" cy="8" r="3" style="stroke:var(--side);fill:var(--side)"/></svg>Pool Snooker<span class="n">600</span></div>
      <div class="sport"><svg class="ico" width="16" height="16"><ellipse cx="8" cy="8" rx="4.5" ry="7"/><path d="M8 4v8M6.5 6h3M6.5 8h3M6.5 10h3"/></svg>Rugby<span class="n">600</span></div>
      <div class="sport"><svg class="ico" width="16" height="16"><circle cx="8" cy="8" r="6.5"/><path d="M8 1.5c-1 4 1 7 6 8M8 8c-3 1-5 3-5.5 5M8 8c2-2 2-5 .5-6.5"/></svg>Volleyball<span class="n">600</span></div>
      <div class="sport"><svg class="ico" width="16" height="16"><path d="M8 1v14M2 4.5l12 7M2 11.5l12-7M6 2.5l2 2 2-2M6 13.5l2-2 2 2"/></svg>Winter Sports<span class="n">600</span></div>
    </div>
    <div class="tabs abs" style="top:972px"><span class="on">Ticket</span><span class="off">Parlay</span></div>
    <div class="bar-under abs"></div>
    <div class="sb-head abs" style="top:1025px">My Bets</div>
    <div class="mybets abs"></div>
    <div class="refresh-s abs">↻ &nbsp;Refresh</div>
    <div class="pending abs">- No Pending Bets -</div>
    <div class="viewall abs">View All</div>
  </aside>

  <section class="board live-board abs" style="top:190px">
    <div class="board-bar"><span class="tab">Today - Live</span><span class="cnt">↻ 38</span><span class="sel">🏆︎ Select League</span></div>
    <div class="grid col-head">
      <div class="span2">Time</div><div class="span2">Event</div>
      <div class="ft">Full Time</div><div class="fh">First Half</div><div class="more">+ More</div>
      <div>A 1x2</div><div>HDP</div><div>OU</div><div>1x2</div><div>HDP</div><div>OU</div><div>1X2</div>
    </div>
    <div class="league"><span class="star">★</span>Southern Coast Premier League</div>
    <div class="event"><div class="c-time"><svg width="14" height="12"><rect x="0" y="5" width="3" height="7" fill="#fff"/><rect x="5" y="1" width="3" height="11" fill="#fff"/><rect x="10" y="3" width="3" height="9" fill="#fff"/></svg><span class="kick">16:30</span><span class="live">Live</span></div><div class="c-event"><span class="star">★</span><div class="teams"><span class="home">Harbour Point Sailors</span><span class="away">Riverton Rangers</span></div></div><div class="c-ft"><span class="hc">0-0.5</span><span class="odds hdp"><b>0.77</b><i>-0.95</i></span><span class="line">6-6.5</span><span class="oul">o<br>u</span><span class="odds ou"><i>-0.85</i><b>0.65</b></span></div><div class="c-fh"></div><div class="c-more"><svg width="9" height="12"><path d="M4.5 0L9 5H0zM4.5 12L0 7h9z" fill="#fff"/></svg>13</div></div>
  </section>

  <section class="board std-board abs" style="top:378px">
    <div class="board-bar"><span class="tab">Today - Live</span><span class="cnt">↻ 38</span><span class="sel">🏆︎ Select League</span></div>
    <div class="grid col-head">
      <div class="span2">Time</div><div class="span2">Event</div>
      <div class="ft">Full Time</div><div class="fh">First Half</div><div class="more">+ More</div>
      <div>A 1x2</div><div>HDP</div><div>OU</div><div>1x2</div><div>HDP</div><div>OU</div><div>1X2</div>
    </div>
    <div class="league"><span class="star">★</span>Southern Coast Premier League</div>
    <div class="event"><div class="c-time"><svg width="14" height="12"><rect x="0" y="5" width="3" height="7" fill="#fff"/><rect x="5" y="1" width="3" height="11" fill="#fff"/><rect x="10" y="3" width="3" height="9" fill="#fff"/></svg><span class="kick">16:30</span><span class="live">Live</span></div><div class="c-event"><span class="star">★</span><div class="teams"><span class="home">Harbour Point Sailors</span><span class="away">Riverton Rangers</span><span>Draw</span></div></div><div class="c-ft"><span class="hc">0-0.5</span><span class="odds hdp"><b>0.77</b><i>-0.95</i></span><span class="line">6-6.5</span><span class="oul">o<br>u</span><span class="odds ou"><i>-0.85</i><b>0.65</b></span></div><div class="c-fh"></div><div class="c-more"><svg width="9" height="12"><path d="M4.5 0L9 5H0zM4.5 12L0 7h9z" fill="#fff"/></svg>13</div></div>
    <div class="league"><span class="star">★</span>Southern Coast Premier League</div>
    <div class="event"><div class="c-time"><svg width="14" height="12"><rect x="0" y="5" width="3" height="7" fill="#fff"/><rect x="5" y="1" width="3" height="11" fill="#fff"/><rect x="10" y="3" width="3" height="9" fill="#fff"/></svg><span class="kick">16:30</span><span class="live">Live</span></div><div class="c-event"><span class="star">★</span><div class="teams"><span class="home">Harbour Point Sailors</span><span class="away">Riverton Rangers</span><span>Draw</span></div></div><div class="c-ft"><span class="hc">0-0.5</span><span class="odds hdp"><b>0.77</b><i>-0.95</i></span><span class="line">6-6.5</span><span class="oul">o<br>u</span><span class="odds ou"><i>-0.85</i><b>0.65</b></span></div><div class="c-fh"></div><div class="c-more"><svg width="9" height="12"><path d="M4.5 0L9 5H0zM4.5 12L0 7h9z" fill="#fff"/></svg>13</div></div>
    <div class="event"><div class="c-time"><svg width="14" height="12"><rect x="0" y="5" width="3" height="7" fill="#fff"/><rect x="5" y="1" width="3" height="11" fill="#fff"/><rect x="10" y="3" width="3" height="9" fill="#fff"/></svg><span class="kick">16:30</span><span class="live">Live</span></div><div class="c-event"><span class="star">★</span><div class="teams"><span class="home">Harbour Point Sailors</span><span class="away">Riverton Rangers</span><span>Draw</span></div></div><div class="c-ft"><span class="hc">0-0.5</span><span class="odds hdp"><b>0.77</b><i>-0.95</i></span><span class="line">6-6.5</span><span class="oul">o<br>u</span><span class="odds ou"><i>-0.85</i><b>0.65</b></span></div><div class="c-fh"></div><div class="c-more"><svg width="9" height="12"><path d="M4.5 0L9 5H0zM4.5 12L0 7h9z" fill="#fff"/></svg>13</div></div>
    <div class="event"><div class="c-time"><svg width="14" height="12"><rect x="0" y="5" width="3" height="7" fill="#fff"/><rect x="5" y="1" width="3" height="11" fill="#fff"/><rect x="10" y="3" width="3" height="9" fill="#fff"/></svg><span class="kick">16:30</span><span class="live">Live</span></div><div class="c-event"><span class="star">★</span><div class="teams"><span class="home">Harbour Point Sailors</span><span class="away">Riverton Rangers</span><span>Draw</span></div></div><div class="c-ft"><span class="hc">0-0.5</span><span class="odds hdp"><b>0.77</b><i>-0.95</i></span><span class="line">6-6.5</span><span class="oul">o<br>u</span><span class="odds ou"><i>-0.85</i><b>0.65</b></span></div><div class="c-fh"></div><div class="c-more"><svg width="9" height="12"><path d="M4.5 0L9 5H0zM4.5 12L0 7h9z" fill="#fff"/></svg>13</div></div>
    <div class="league"><span class="star">★</span>Southern Coast Premier League</div>
    <div class="event"><div class="c-time"><svg width="14" height="12"><rect x="0" y="5" width="3" height="7" fill="#fff"/><rect x="5" y="1" width="3" height="11" fill="#fff"/><rect x="10" y="3" width="3" height="9" fill="#fff"/></svg><span class="kick">16:30</span><span class="live">Live</span></div><div class="c-event"><span class="star">★</span><div class="teams"><span class="home">Harbour Point Sailors</span><span class="away">Riverton Rangers</span><span>Draw</span></div></div><div class="c-ft"><span class="hc">0-0.5</span><span class="odds hdp"><b>0.77</b><i>-0.95</i></span><span class="line">6-6.5</span><span class="oul">o<br>u</span><span class="odds ou"><i>-0.85</i><b>0.65</b></span></div><div class="c-fh"></div><div class="c-more"><svg width="9" height="12"><path d="M4.5 0L9 5H0zM4.5 12L0 7h9z" fill="#fff"/></svg>13</div></div>
    <div class="league"><span class="star">★</span>Southern Coast Premier League</div>
    <div class="event"><div class="c-time"><svg width="14" height="12"><rect x="0" y="5" width="3" height="7" fill="#fff"/><rect x="5" y="1" width="3" height="11" fill="#fff"/><rect x="10" y="3" width="3" height="9" fill="#fff"/></svg><span class="kick">16:30</span><span class="live">Live</span></div><div class="c-event"><span class="star">★</span><div class="teams"><span class="home">Harbour Point Sailors</span><span class="away">Riverton Rangers</span><span>Draw</span></div></div><div class="c-ft"><span class="hc">0-0.5</span><span class="odds hdp"><b>0.77</b><i>-0.95</i></span><span class="line">6-6.5</span><span class="oul">o<br>u</span><span class="odds ou"><i>-0.85</i><b>0.65</b></span></div><div class="c-fh"></div><div class="c-more"><svg width="9" height="12"><path d="M4.5 0L9 5H0zM4.5 12L0 7h9z" fill="#fff"/></svg>13</div></div>
    <div class="event"><div class="c-time"><svg width="14" height="12"><rect x="0" y="5" width="3" height="7" fill="#fff"/><rect x="5" y="1" width="3" height="11" fill="#fff"/><rect x="10" y="3" width="3" height="9" fill="#fff"/></svg><span class="kick">16:30</span><span class="live">Live</span></div><div class="c-event"><span class="star">★</span><div class="teams"><span class="home">Harbour Point Sailors</span><span class="away">Riverton Rangers</span><span>Draw</span></div></div><div class="c-ft"><span class="hc">0-0.5</span><span class="odds hdp"><b>0.77</b><i>-0.95</i></span><span class="line">6-6.5</span><span class="oul">o<br>u</span><span class="odds ou"><i>-0.85</i><b>0.65</b></span></div><div class="c-fh"></div><div class="c-more"><svg width="9" height="12"><path d="M4.5 0L9 5H0zM4.5 12L0 7h9z" fill="#fff"/></svg>13</div></div>
    <div class="event"><div class="c-time"><svg width="14" height="12"><rect x="0" y="5" width="3" height="7" fill="#fff"/><rect x="5" y="1" width="3" height="11" fill="#fff"/><rect x="10" y="3" width="3" height="9" fill="#fff"/></svg><span class="kick">16:30</span><span class="live">Live</span></div><div class="c-event"><span class="star">★</span><div class="teams"><span class="home">Harbour Point Sailors</span><span class="away">Riverton Rangers</span><span>Draw</span></div></div><div class="c-ft"><span class="hc">0-0.5</span><span class="odds hdp"><b>0.77</b><i>-0.95</i></span><span class="line">6-6.5</span><span class="oul">o<br>u</span><span class="odds ou"><i>-0.85</i><b>0.65</b></span></div><div class="c-fh"></div><div class="c-more"><svg width="9" height="12"><path d="M4.5 0L9 5H0zM4.5 12L0 7h9z" fill="#fff"/></svg>13</div></div>
    <div class="event"><div class="c-time"><svg width="14" height="12"><rect x="0" y="5" width="3" height="7" fill="#fff"/><rect x="5" y="1" width="3" height="11" fill="#fff"/><rect x="10" y="3" width="3" height="9" fill="#fff"/></svg><span class="kick">16:30</span><span class="live">Live</span></div><div class="c-event"><span class="star">★</span><div class="teams"><span class="home">Harbour Point Sailors</span><span class="away">Riverton Rangers</span><span>Draw</span></div></div><div class="c-ft"><span class="hc">0-0.5</span><span class="odds hdp"><b>0.77</b><i>-0.95</i></span><span class="line">6-6.5</span><span class="oul">o<br>u</span><span class="odds ou"><i>-0.85</i><b>0.65</b></span></div><div class="c-fh"></div><div class="c-more"><svg width="9" height="12"><path d="M4.5 0L9 5H0zM4.5 12L0 7h9z" fill="#fff"/></svg>13</div></div>
    <div class="event"><div class="c-time"><svg width="14" height="12"><rect x="0" y="5" width="3" height="7" fill="#fff"/><rect x="5" y="1" width="3" height="11" fill="#fff"/><rect x="10" y="3" width="3" height="9" fill="#fff"/></svg><span class="kick">16:30</span><span class="live">Live</span></div><div class="c-event"><span class="star">★</span><div class="teams"><span class="home">Harbour Point Sailors</span><span class="away">Riverton Rangers</span><span>Draw</span></div></div><div class="c-ft"><span class="hc">0-0.5</span><span class="odds hdp"><b>0.77</b><i>-0.95</i></span><span class="line">6-6.5</span><span class="oul">o<br>u</span><span class="odds ou"><i>-0.85</i><b>0.65</b></span></div><div class="c-fh"></div><div class="c-more"><svg width="9" height="12"><path d="M4.5 0L9 5H0zM4.5 12L0 7h9z" fill="#fff"/></svg>13</div></div>
    <div class="event"><div class="c-time"><svg width="14" height="12"><rect x="0" y="5" width="3" height="7" fill="#fff"/><rect x="5" y="1" width="3" height="11" fill="#fff"/><rect x="10" y="3" width="3" height="9" fill="#fff"/></svg><span class="kick">16:30</span><span class="live">Live</span></div><div class="c-event"><span class="star">★</span><div class="teams"><span class="home">Harbour Point Sailors</span><span class="away">Riverton Rangers</span><span>Draw</span></div></div><div class="c-ft"><span class="hc">0-0.5</span><span class="odds hdp"><b>0.77</b><i>-0.95</i></span><span class="line">6-6.5</span><span class="oul">o<br>u</span><span class="odds ou"><i>-0.85</i><b>0.65</b></span></div><div class="c-fh"></div><div class="c-more"><svg width="9" height="12"><path d="M4.5 0L9 5H0zM4.5 12L0 7h9z" fill="#fff"/></svg>13</div></div>
    <div class="event"><div class="c-time"><svg width="14" height="12"><rect x="0" y="5" width="3" height="7" fill="#fff"/><rect x="5" y="1" width="3" height="11" fill="#fff"/><rect x="10" y="3" width="3" height="9" fill="#fff"/></svg><span class="kick">16:30</span><span class="live">Live</span></div><div class="c-event"><span class="star">★</span><div class="teams"><span class="home">Harbour Point Sailors</span><span class="away">Riverton Rangers</span><span>Draw</span></div></div><div class="c-ft"><span class="hc">0-0.5</span><span class="odds hdp"><b>0.77</b><i>-0.95</i></span><span class="line">6-6.5</span><span class="oul">o<br>u</span><span class="odds ou"><i>-0.85</i><b>0.65</b></span></div><div class="c-fh"></div><div class="c-more"><svg width="9" height="12"><path d="M4.5 0L9 5H0zM4.5 12L0 7h9z" fill="#fff"/></svg>13</div></div>
    <div class="event"><div class="c-time"><svg width="14" height="12"><rect x="0" y="5" width="3" height="7" fill="#fff"/><rect x="5" y="1" width="3" height="11" fill="#fff"/><rect x="10" y="3" width="3" height="9" fill="#fff"/></svg><span class="kick">16:30</span><span class="live">Live</span></div><div class="c-event"><span class="star">★</span><div class="teams"><span class="home">Harbour Point Sailors</span><span class="away">Riverton Rangers</span><span>Draw</span></div></div><div class="c-ft"><span class="hc">0-0.5</span><span class="odds hdp"><b>0.77</b><i>-0.95</i></span><span class="line">6-6.5</span><span class="oul">o<br>u</span><span class="odds ou"><i>-0.85</i><b>0.65</b></span></div><div class="c-fh"></div><div class="c-more"><svg width="9" height="12"><path d="M4.5 0L9 5H0zM4.5 12L0 7h9z" fill="#fff"/></svg>13</div></div>
  </section>

  <footer class="footer abs">
    <span>Betting Rules</span><span>Contact Us</span><span>Privacy Policy</span><span>Responsible Gambling</span><span>Terms &amp; Conditions</span><span>Tutorials</span>
  </footer>
</div>
</body>
</html>
```